New Jazz Music Album CD Design

Need a contemporary jazz CD cover for my single I will be releasing December 31. Name of the song is called Late Harbor . Artist Name is Dasmon Kreel. Website is Http://DasmonK.com. Please find a way to incorporate my attached logo and add my attached picture somewhere to the album art. Front Cover Demensions width 1423 pixel height 1411 pixels RGB 16 color no bleed. Inside Front Cover Demensions width 1423 pixel height 1411 pixels RGB 16 color no bleed. Disc dimensions Diameter: 1394 pixels RGB 16 bit color. Back tray card with 2 spines width (includes 2 spines) 1772 pixels height 1385 pixels spine width 74 pixels.
Updates

The images in the path below will also suffice for the design https://filebox-share.example/f/s!QpZrTwmN8XcVbLo3Hd72JkYe

Target Market(s)

Age group 35 and older. Smooth jazz listeners.

Industry/Entity Type

Music Download

Font styles to use
Serif
Sans Serif

Colors

Designer to choose colors to be used in the design.

Requirements
Must have
• Song title Late Harbor
• Artist name: Dasmon K
• Attached Logo
• Website: DasmonK.com
Nice to have
• NA
Should not have
• Na

```html
<!DOCTYPE html>
<html lang="en">
<head>
<meta charset="utf-8">
<title>Dasmon K — Late Harbor</title>
<link href="https://fonts.googleapis.com/css2?family=Playfair+Display:wght@400;900&family=Montserrat:wght@400&display=swap" rel="stylesheet">
<style>
  :root {
    --wall-light: #c4baac;
    --wall-mid: #ab9f90;
    --wall-dark: #7a7166;
    --bench: #9a9c9c;
    --ground: #bdbab4;
    --blazer: #eeeeec;
    --denim: #2c3a52;
    --brand-grey: #8e9093;
    --brand-ink: #2b2b2b;
    --accent-red: #c8161d;
    --title-white: #ffffff;
    --site-ink: #2b2b2b;
  }
  html, body {
    margin: 0;
    padding: 0;
    width: 1200px;
    height: 1200px;
    overflow: hidden;
    background: var(--wall-mid);
  }
  .cover {
    position: relative;
    width: 1200px;
    height: 1200px;
    overflow: hidden;
  }
  .cover__photo {
    position: absolute;
    inset: 0;
    background:
      radial-gradient(ellipse 230px 300px at 66% 36%, rgba(238,238,236,0.95) 0%, rgba(238,238,236,0.7) 55%, rgba(238,238,236,0) 100%),
      radial-gradient(ellipse 260px 260px at 68% 76%, rgba(44,58,82,0.95) 0%, rgba(44,58,82,0.6) 60%, rgba(44,58,82,0) 100%),
      linear-gradient(180deg,
        var(--wall-light) 0%,
        var(--wall-mid) 57%,
        var(--bench) 60%,
        var(--bench) 68%,
        var(--wall-dark) 70%,
        var(--wall-dark) 91%,
        var(--ground) 93%,
        var(--ground) 100%);
  }
  .brand {
    position: absolute;
    left: 72px;
    top: 136px;
    display: flex;
    align-items: center;
    gap: 16px;
  }
  .brand__mark {
    width: 30px;
    height: 30px;
    background: var(--brand-grey);
  }
  .brand__name {
    font-family: "Montserrat", sans-serif;
    font-weight: 400;
    font-size: 46px;
    line-height: 1;
    color: var(--brand-ink);
  }
  .artist {
    position: absolute;
    left: 73px;
    top: 588px;
    margin: 0;
    font-family: "Playfair Display", serif;
    font-weight: 900;
    font-size: 93px;
    line-height: 1;
    letter-spacing: -1px;
    color: var(--accent-red);
    white-space: nowrap;
  }
  .title {
    position: absolute;
    left: 70px;
    top: 819px;
    margin: 0;
    font-family: "Playfair Display", serif;
    font-weight: 900;
    font-size: 250px;
    line-height: 1;
    letter-spacing: -6px;
    color: var(--title-white);
    white-space: nowrap;
    transform: scaleX(0.71);
    transform-origin: left top;
  }
  .site {
    position: absolute;
    left: 74px;
    top: 1140px;
    font-family: "Montserrat", sans-serif;
    font-weight: 400;
    font-size: 36px;
    line-height: 1;
    color: var(--site-ink);
  }
</style>
</head>
<body>
  <main class="cover">
    <div class="cover__photo" role="img" aria-label="Portrait of the artist in a white blazer and dark jeans, smiling, seated on a concrete bench against a board-formed concrete wall"></div>

    <div class="brand">
      <span class="brand__mark"></span>
      <span class="brand__name">Dasmon K</span>
    </div>

    <h2 class="artist">DASMON K</h2>
    <h1 class="title">Late Harbor</h1>
    <div class="site">DasmonK.com</div>
  </main>
</body>
</html>
```